Website for BQM CIVIL

looking for a clean crisp website outlining what we do, we are a telecommunications cable installer working on internet cabling, i am just looking for imagery and we will complete content

i need a

home page template
services tab (4 services)
Rod / Roping
Hauling
Civil
Surveying
Contact Us Page
Testimonials Page
About Us
Our Vision
History

Target Market(s)

Telecommunication Companies

Industry/Entity Type

Telecommunications

Requirements
Must have
• images and logo themed colors

this is main project we are working on

http://www.vorlyx.com.au/

this is an example of our competitor site in the same field, we are much smaller though

```html
<!DOCTYPE html>
<html lang="en">
<head>
<meta charset="utf-8">
<title>BQM CIVIL</title>
<link rel="stylesheet" href="https://fonts.googleapis.com/css2?family=Source+Sans+3:wght@300;400;600&display=swap">
<style>
:root{
  --orange:#f07d1a;
  --orange-dark:#ea6a0a;
  --navy:#0d3a73;
  --navy-light:#1f5599;
  --ink:#3c3c3c;
  --muted:#6a6a6a;
  --line:#dcdcdc;
  --bg:#ffffff;
  --logo-grey:#6b6e72;
}
*{box-sizing:border-box;margin:0;padding:0}
html,body{width:1200px;height:1097px;overflow:hidden;background:var(--bg)}
body{font-family:"Source Sans 3",sans-serif;color:var(--ink);position:relative}

.site-header{position:absolute;left:0;top:0;width:1200px;height:132px;
  background:linear-gradient(#fff 60%,#f4f4f4);border-bottom:1px solid var(--line)}
.brand{position:absolute;left:60px;top:46px;display:flex;align-items:center;gap:10px;
  font-size:40px;font-weight:600;color:var(--logo-grey);letter-spacing:1px;line-height:1}
.brand-dot{width:16px;height:16px;border-radius:50%;background:var(--orange)}
.social{position:absolute;left:755px;top:26px;display:flex;gap:6px}
.social span{width:25px;height:25px;border-radius:3px;background:#3d7cc9}
.social span:first-child{background:#3aa6e0}
.search{position:absolute;left:862px;top:22px;width:265px;height:35px;border:1px solid #c8c8c8;
  border-radius:18px;background:#fff;font-size:13px;font-style:italic;color:#888;padding:8px 16px}
.search svg{position:absolute;right:12px;top:8px}
.main-nav{position:absolute;right:82px;top:86px;display:flex;font-size:17px;font-weight:300;color:#333}
.main-nav a{color:inherit;text-decoration:none;padding:0 17px;border-left:1px solid #bbb;line-height:20px}
.main-nav a:first-child{border-left:0}
.main-nav a:last-child{padding-right:0}

.hero{position:absolute;left:60px;top:153px;width:1080px;height:377px;border-radius:4px 4px 0 0;
  background:linear-gradient(100deg,#d9d9d6 0%,#ecd3c0 25%,#e7e5e2 45%,#c9a58f 55%,#eef0f1 75%,#fafafa 100%)}
.tabs{position:absolute;left:60px;top:530px;width:1078px;height:92px;display:flex}
.tab{flex:1;border:1px solid var(--line);border-left:0;border-radius:0 0 4px 4px;padding:20px 24px;
  background:linear-gradient(#fff,#f7f7f7);box-shadow:0 6px 10px rgba(0,0,0,.05)}
.tab h3{font-size:19px;font-weight:400;color:#333;line-height:22px}
.tab p{font-size:14px;font-weight:300;color:var(--muted);margin-top:4px}
.tab.active{background:linear-gradient(var(--orange),var(--orange-dark));border-color:var(--orange)}
.tab.active h3,.tab.active p{color:#fff}

.services-title{position:absolute;left:65px;top:670px;font-size:24px;font-weight:300;color:var(--orange)}
.services{position:absolute;left:64px;top:722px;width:1080px}
.service{position:absolute;top:0;width:250px}
.service .thumb{position:absolute;left:0;top:0;width:100px;height:103px}
.service h4{position:absolute;left:112px;top:-2px;font-size:20px;font-weight:400;color:#333;white-space:nowrap}
.service p{position:absolute;left:112px;top:30px;width:140px;font-size:13.5px;font-weight:300;line-height:22px;color:var(--muted)}
.btn{position:absolute;left:110px;top:146px;width:94px;height:31px;border-radius:3px;
  background:linear-gradient(var(--navy-light),var(--navy));color:#fff;font-size:12px;
  text-align:center;line-height:31px;text-transform:uppercase;letter-spacing:-.2px}

.site-footer{position:absolute;left:60px;top:970px;width:1080px;height:127px;border-top:1px solid #e8e8e8}
.footer-nav{position:absolute;left:10px;top:36px;display:flex;font-size:14.5px;color:#444}
.footer-nav a{color:inherit;text-decoration:none;padding:0 8px;border-left:1px solid #888;line-height:15px}
.footer-nav a:first-child{border-left:0;padding-left:0}
.copyright{position:absolute;left:10px;top:70px;font-size:13px;font-weight:300;color:var(--muted)}
.footer-brand{position:absolute;right:24px;top:44px;font-size:30px;font-weight:600;color:var(--logo-grey);letter-spacing:1px}
</style>
</head>
<body>
<header class="site-header">
  <div class="brand"><span class="brand-dot"></span>BQM CIVIL</div>
  <div class="social"><span></span><span></span><span></span></div>
  <div class="search">Search here..
    <svg width="18" height="18" viewBox="0 0 18 18"><circle cx="7.5" cy="7.5" r="5" fill="none" stroke="#999" stroke-width="2.4"/><line x1="11" y1="11" x2="16" y2="16" stroke="#999" stroke-width="3" stroke-linecap="round"/></svg>
  </div>
  <nav class="main-nav">
    <a href="#">Home</a><a href="#">Services</a><a href="#">Contact Us</a><a href="#">Testimonials</a><a href="#">About Us</a><a href="#">Our Vision</a><a href="#">History</a>
  </nav>
</header>

<div class="hero" role="img" aria-label="Smiling couple lying down using a laptop computer"></div>
<div class="tabs">
  <div class="tab active"><h3>Mauris vel lacus</h3><p>Etiam est nunc venenatis tristique</p></div>
  <div class="tab"><h3>Nullam enim leo</h3><p>Curabitur vel mi sit amet magna</p></div>
  <div class="tab"><h3>Suspendisse quam leo</h3><p>Curabitur vel mi sit amet magna</p></div>
  <div class="tab"><h3>Vivamus porttitor</h3><p>Curabitur vel mi sit amet magna</p></div>
</div>

<h2 class="services-title">Services We Provide</h2>
<section class="services">
  <div class="service" style="left:0">
    <div class="thumb" role="img" aria-label="Blue network cables plugged into a switch" style="background:linear-gradient(135deg,#8a8f96,#5aa8d8 55%,#cfd3d8)"></div>
    <h4>Rod / Roping</h4>
    <p>Nunc tempus felis vitae urna. Vivamus porttitor, g, purus nisi eleifend libero, a tempus libero lectus feugiat felis.</p>
    <a class="btn" href="#">Read More</a>
  </div>
  <div class="service" style="left:275px">
    <div class="thumb" role="img" aria-label="Family carrying moving boxes" style="background:linear-gradient(135deg,#9fb58a,#c9a97e 55%,#e6e2da)"></div>
    <h4>Hauling</h4>
    <p>Nunc tempus felis vitae urna. Vivamus porttitor, g, purus nisi eleifend libero, a tempus libero lectus feugiat felis.</p>
    <a class="btn" href="#">Read More</a>
  </div>
  <div class="service" style="left:549px">
    <div class="thumb" role="img" aria-label="Worker in hard hat and safety vest" style="background:linear-gradient(135deg,#d9c9b5,#b8d44a 55%,#a88f78)"></div>
    <h4>Civil</h4>
    <p>Nunc tempus felis vitae urna. Vivamus porttitor, g, purus nisi eleifend libero, a tempus libero lectus feugiat felis.</p>
    <a class="btn" href="#">Read More</a>
  </div>
  <div class="service" style="left:825px">
    <div class="thumb" role="img" aria-label="Team of surveyors in hard hats reviewing plans" style="background:linear-gradient(135deg,#e9ecef,#e0a04a 50%,#4a4f58)"></div>
    <h4>Surveying</h4>
    <p>Nunc tempus felis vitae urna. Vivamus porttitor, g, purus nisi eleifend libero, a tempus libero lectus feugiat felis.</p>
    <a class="btn" href="#">Read More</a>
  </div>
</section>

<footer class="site-footer">
  <nav class="footer-nav">
    <a href="#">Home</a><a href="#">Services</a><a href="#">Contact Us</a><a href="#">Testimonials</a><a href="#">About Us</a><a href="#">Our Vision</a><a href="#">History</a>
  </nav>
  <p class="copyright">Copyright © 2013 Company Name.&nbsp; All right reserved</p>
  <div class="footer-brand">BQM CIVIL</div>
</footer>
</body>
</html>
```